Halvorn Analytics, Inc. Site Design Project

Halvorn Analytics, Inc is my private and small research office.
This naming shows:
We investigate every(*: asterisk) issue to support society.
We investigate "a star risk" which means every critical things for example, information security, branding, public communication - to understand for our clients - especially innovative person.
Last year, we had faced the great disaster in Japan, we investigated the damaged place, schools, and local governments, and supported communities like PLUMvaskel.
So I want to get a high concept sites with good logo and to use card, website, and our letter.
Reason: We would like to look for more competitive candidates.
I uploaded the latest logo. If you have any idea to adapt it to your design, I appreciate it.
Target Market(s)
* marketing section of leading companies(enterprises)
* promotion agencies of government
* futurist and researcher
* business managers
Industry/Entity Type
Communication
Logo Text
for desirable future
Look and feel
Each slider illustrates characteristics of the customer's brand and the style your logo design should communicate.

```html
<!DOCTYPE html>
<html lang="en">
<head>
<meta charset="utf-8">
<title>Halvorn Analytics, Inc</title>
<link href="https://fonts.googleapis.com/css2?family=PT+Sans:wght@400;700&display=swap" rel="stylesheet">
<style>
:root{
  --page:#f4f4f4;
  --ink-dark:#13231c;
  --ink-deep:#0f1c16;
  --ribbon:#2d4a3b;
  --ribbon-edge:#1d3328;
  --tile:#8fb59c;
  --search:#2b4a3d;
  --cream-top:#fdf8f2;
  --cream-bottom:#f5ede2;
  --beige-top:#f1ece1;
  --beige-bottom:#ddd6c2;
  --body-text:#6d6a66;
  --band-text:#c9d0cc;
  --olive:#2b2a10;
  --slate:#858580;
  --picture-label:#2b2a10;
  --footer-link:#3d4c42;
  --footer-text:#3a4a41;
  --partner-blue:#1d5fa8;
  --white:#ffffff;
}
*{margin:0;padding:0;box-sizing:border-box}
html,body{width:1020px;height:1200px;overflow:hidden}
body{position:relative;background:var(--page);font-family:"PT Sans",sans-serif;color:var(--body-text)}
.abs{position:absolute}
.column-edge{left:32px;top:0;width:942px;height:1061px;border-left:1px solid #dcdcdc;border-right:1px solid #dcdcdc;background:var(--white)}
.masthead{left:40px;top:0;width:849px;height:94px;background:var(--ink-dark)}
.brand{left:68px;top:26px;display:flex;align-items:center;gap:10px;font-weight:700;font-size:31px;color:#dde3df;letter-spacing:.5px}
.brand-dot{width:18px;height:18px;border-radius:50%;background:#e8a531}
.ribbon{left:898px;top:0;width:42px;height:102px}
.social{left:905px;width:28px;display:flex;flex-direction:column;gap:7px}
.social span{display:block;width:20px;height:18px;margin:0 auto;background:var(--tile);border-radius:2px}
.nav{left:83px;top:101px;display:flex;font-weight:700;font-size:17px;color:#1f2f27}
.nav a{color:inherit;text-decoration:none;padding:1px 11px 3px;border-left:1px dashed #40544a;position:relative}
.nav a:last-child{border-right:1px dashed #40544a}
.nav a.current::after{content:"";position:absolute;left:50%;bottom:-8px;margin-left:-5px;border:5px solid transparent;border-bottom-color:#1f2f27}
.nav-rule{left:59px;top:127px;width:883px;height:2px;background:#1f2f27}
.search{width:192px;height:18px;background:var(--search)}
.intro{left:32px;top:130px;width:942px;height:272px;background:linear-gradient(var(--cream-top),var(--cream-bottom))}
.picture{display:flex;align-items:center;justify-content:center;font-weight:700;font-size:31px;color:var(--picture-label)}
.picture.dark{background:var(--olive);color:#e8e6da;text-shadow:0 1px 3px #000}
.picture.slate{background:var(--slate)}
.intro-text{left:373px;top:154px;width:402px;font-size:15.8px;line-height:20.3px;text-align:justify;height:226px;overflow:hidden}
.intro-text p+p{margin-top:20px}
.partner{left:805px;width:126px;background:var(--white);box-shadow:0 0 3px #e5ddd0;display:flex;align-items:center;justify-content:center}
.partner span{width:30px;height:20px;background:var(--partner-blue)}
.feature-band{left:0;top:404px;width:1020px;height:232px;background:var(--ink-dark)}
.feature-text{left:310px;top:462px;width:564px;font-size:18px;line-height:23.3px;color:var(--band-text);text-align:justify;height:140px;overflow:hidden}
.divider{left:60px;top:639px;width:882px;border-top:1px dashed #8a8a80}
.stories{left:32px;top:640px;width:942px;height:421px;background:linear-gradient(var(--beige-top),var(--beige-bottom))}
.story{left:83px;width:613px;font-size:15.6px;line-height:20.4px;text-align:justify}
.footer{left:0;top:1061px;width:1020px;height:139px;background:var(--ink-deep)}
.footer-links{left:71px;top:1071px;display:flex;flex-direction:column;font-weight:700;font-size:16px;line-height:20.4px;color:var(--footer-link)}
.footer-rule{left:160px;top:1075px;height:120px;border-left:1px dashed #2a3a32}
.footer-text{left:185px;top:1111px;width:673px;font-size:11.4px;line-height:13.6px;color:var(--footer-text);text-align:justify}
.copyright{left:0;top:1186px;width:1020px;text-align:center;font-size:8px;color:#4a5a50}
</style>
</head>
<body>
<div class="abs column-edge"></div>

<header>
  <div class="abs masthead"></div>
  <div class="abs brand"><span class="brand-dot"></span>HALVORN ANALYTICS, INC</div>
  <svg class="abs ribbon" viewBox="0 0 42 102" aria-hidden="true"><path d="M0 0H42V102L21 88 0 102Z" fill="var(--ribbon)"/><path d="M4 0V92M38 0V92" stroke="var(--ribbon-edge)" stroke-dasharray="2 2"/></svg>
  <div class="abs social" style="top:10px" aria-label="Social links"><span></span><span></span><span></span></div>
  <nav class="abs nav"><a class="current" href="#">Home</a><a href="#">Link1</a><a href="#">Link2</a><a href="#">About us</a><a href="#">Contact</a></nav>
  <div class="abs search" style="left:666px;top:106px"></div>
  <svg class="abs" style="left:860px;top:106px" width="18" height="18" viewBox="0 0 18 18" aria-hidden="true"><circle cx="7" cy="7" r="5" fill="none" stroke="#6fa882" stroke-width="2"/><path d="M11 11l5 5" stroke="#6fa882" stroke-width="2.5"/></svg>
  <div class="abs nav-rule"></div>
</header>

<section>
  <div class="abs intro"></div>
  <div class="abs picture dark" style="left:83px;top:154px;width:272px;height:231px" role="img" aria-label="Featured photograph">PICTURE</div>
  <div class="abs intro-text">
    <p>Lorem Ipsum is simply dummy text of the printing and typesetting industry.</p>
    <p>Lorem Ipsum has been the industry's standard dummy text ever since the 1500s, when an unknown printer took a galley of type and scrambled it to make a type specimen book. It has survived not only five centuries, but also the leap into electronic typesetting, remaining essentially unchanged. It was popularised in the 1960s with the release of Typeleaf sheets containing Lorem Ipsum passages, and more recently with desktop publishing</p>
  </div>
  <div class="abs partner" style="top:143px;height:77px"><span></span></div>
  <div class="abs partner" style="top:226px;height:77px"><span></span></div>
  <div class="abs partner" style="top:312px;height:77px"><span></span></div>
</section>

<section>
  <div class="abs feature-band"></div>
  <div class="abs picture slate" style="left:83px;top:464px;width:199px;height:142px" role="img" aria-label="Feature photograph">PICTURE</div>
  <p class="abs feature-text">Lorem Ipsum is simply dummy text of the printing and typesetting industry. Lorem Ipsum has been the industry's standard dummy text ever since the 1500s, when an unknown printer took a galley of type and scrambled it to make a type specimen book. It has survived not only five centuries, but also the leap into electronic typesetting, remaining essentially unchanged. It was popularised in the 1960s with the release of</p>
  <div class="abs divider"></div>
</section>

<section>
  <div class="abs stories"></div>
  <p class="abs story" style="top:690px">Lorem Ipsum is simply dummy text o the printing and typesetting industry. Lorem Ipsum has been the industry's standard dummy text ever since the 1500s, when an unknown printer took a galley of type and scrambled it to make a type specimen book. It has survived not only five centuries, but also the leap into electronic typesetting, remaining essentially unchanged. It was popularised in the 1960s with the release of Typeleaf sheets containing Lorem Ipsum passages, and more recently with desktop publishing software like Orvel PageCraft including versions of Lorem Ipsum.</p>
  <div class="abs picture slate" style="left:719px;top:695px;width:179px;height:131px" role="img" aria-label="Story photograph">PICTURE</div>
  <p class="abs story" style="top:854px">Lorem Ipsum is simply dummy text o the printing and typesetting industry. Lorem Ipsum has been the industry's standard dummy text ever since the 1500s, when an unknown printer took a galley of type and scrambled it to make a type specimen book. It has survived not only five centuries, but also the leap into electronic typesetting, remaining essentially unchanged. It was popularised in the 1960s with the release of Typeleaf sheets containing Lorem Ipsum passages, and more recently with desktop publishing software like Orvel PageCraft including versions of Lorem Ipsum.</p>
  <div class="abs picture slate" style="left:719px;top:859px;width:179px;height:131px" role="img" aria-label="Story photograph">PICTURE</div>
</section>

<footer>
  <div class="abs footer"></div>
  <div class="abs footer-links"><span>Home</span><span>Links</span><span>Links</span><span>About us</span><span>Contact</span></div>
  <div class="abs footer-rule"></div>
  <p class="abs footer-text">Lorem Ipsum is simply dummy text of the printing and typesetting industry. Lorem Ipsum has been the industry's standard dummy text ever since the 1500s, when an unknown printer took a galley of type and scrambled it to make a type specimen book. It has survived not only five centuries, but also the leap into electronic typesetting, remaining essentially unchanged.</p>
  <div class="abs search" style="left:647px;top:1076px;width:189px;height:17px"></div>
  <svg class="abs" style="left:839px;top:1075px" width="18" height="18" viewBox="0 0 18 18" aria-hidden="true"><circle cx="7" cy="7" r="5" fill="none" stroke="#6fa882" stroke-width="2"/><path d="M11 11l5 5" stroke="#6fa882" stroke-width="2.5"/></svg>
  <svg class="abs ribbon" style="left:864px;top:1066px;height:100px" viewBox="0 0 42 102" preserveAspectRatio="none" aria-hidden="true"><path d="M0 0H42V102L21 88 0 102Z" fill="var(--ribbon)"/><path d="M4 0V92M38 0V92" stroke="var(--ribbon-edge)" stroke-dasharray="2 2"/></svg>
  <div class="abs social" style="left:871px;top:1078px" aria-label="Social links"><span></span><span></span><span></span></div>
  <p class="abs copyright">Halvorn Analytics, Inc copyright 2012</p>
</footer>
</body>
</html>
```